Gorgeous A5 Booklet 8pp - Existing Branding

Please transform a PDF text doc into an A5 booklet according to my existing branding, I need it fast.
I need to go to print.
Must be modern, fun, clean and classy design.
I can send images, logos and the .indd for the existing pdf to help you.
Thanks for being awesome!

We are a design agency so it needs to be good...we are too busy to create it.

Front cover can have open paragraph.
Back cover must have contact details
three inside spreads should have the 11 essentials.

The executive summary attached is a good example of the look and feel you can copy.

Please let me know if you have any questions.
Thanks
Light ahead!
:)

Target Market(s)

entreprenuers and small business owners

Industry/Entity Type

Design Agency

Font styles to use
Sans Serif

Colors
e34197
fff5ee
333333
faa54b
acd036
33a6d7

Requirements
Must have
• font is century gothic - no bold
gudea body text
sketch rockwell
seans hand

see website www.brightvane.com.au for branding
or match to pdf attached with origami images

Colours in palette below of only indicative. actual colours are as per website colour strip.
Should not have
• not too pink
not too many stars

```html
<!DOCTYPE html>
<html lang="en">
<head>
<meta charset="utf-8">
<title>Eleven Essentials – Spread 8 to 11</title>
<link href="https://fonts.googleapis.com/css2?family=Arvo:wght@700&family=Gudea:wght@400&display=swap" rel="stylesheet">
<style>
  :root {
    --green: #acd036;
    --pink: #e34197;
    --blue: #2e78bd;
    --orange: #faa54b;
    --teal: #33a6d7;
    --ink: #333333;
    --paper: #ffffff;
    --fold: #e9e9e9;
    --photo-light: #eef0f2;
    --photo-dark: #d3d8dd;
  }
  * { margin: 0; padding: 0; box-sizing: border-box; }
  html, body { width: 1200px; height: 848px; overflow: hidden; background: var(--paper); }
  .spread {
    position: relative; width: 1200px; height: 848px;
    background: linear-gradient(90deg, var(--paper) 0, var(--paper) 590px, var(--fold) 600px, var(--paper) 612px, var(--paper) 100%);
    font-family: "Gudea", Arial, sans-serif;
    color: var(--paper);
  }
  .panel { position: absolute; }
  .panel--green { left: 37px; top: 87px; width: 523px; height: 280px; background: var(--green); }
  .panel--pink { left: 37px; top: 440px; width: 523px; height: 332px; background: var(--pink); }
  .panel--blue { left: 632px; top: 32px; width: 528px; height: 261px; background: var(--blue); }
  .panel--orange { left: 632px; top: 308px; width: 293px; height: 464px; background: var(--orange); }
  .photo {
    position: absolute; left: 940px; top: 308px; width: 260px; height: 464px;
    background: linear-gradient(160deg, var(--photo-light), var(--photo-dark));
  }
  .essential-title {
    position: absolute; font-family: "Arvo", Georgia, serif; font-weight: 700;
    font-size: 23px; line-height: 31px; letter-spacing: 0.5px; color: var(--paper);
  }
  .essential-body {
    position: absolute; font-size: 13.4px; line-height: 17px; text-align: justify;
  }
  .essential-body p + p { margin-top: 17px; }
  .essential-body ul { list-style: none; }
  .essential-body li::before { content: "• "; }
  .badge { position: absolute; overflow: visible; }
  .badge text { font-family: "Arvo", Georgia, serif; font-weight: 700; fill: var(--paper); }
  .footer-strip { position: absolute; left: 0; top: 790px; width: 1200px; height: 7px; display: flex; }
  .footer-strip span { flex: 1; }
  .footer { position: absolute; left: 0; top: 797px; width: 1200px; height: 51px; background: var(--ink); }
  .brand {
    position: absolute; top: 812px; display: flex; align-items: center; gap: 6px;
    font-family: "Gudea", Arial, sans-serif; font-size: 19px; color: var(--pink);
  }
  .brand i { width: 11px; height: 11px; border-radius: 50%; background: var(--pink); display: block; }
  .brand--left { left: 37px; }
  .brand--right { left: 1065px; }
</style>
</head>
<body>
<div class="spread">

  <!-- Essential 8 -->
  <div class="panel panel--green"></div>
  <svg class="badge" style="left:26px;top:38px" width="120" height="100" viewBox="0 0 120 100">
    <path d="M8 50 a52 42 0 1 1 40 41 l-18 9 l4 -14 a52 42 0 0 1 -26 -36z" fill="var(--teal)"/>
    <ellipse cx="60" cy="50" rx="45" ry="35" fill="none" stroke="#fff" stroke-width="1.5" stroke-dasharray="3 3"/>
    <text x="60" y="72" font-size="58" text-anchor="middle">8.</text>
  </svg>
  <h2 class="essential-title" style="left:152px;top:102px">Mobile friendly design</h2>
  <div class="essential-body" style="left:64px;top:148px;width:474px">
    <p>25% of people on the internet at any given moment are using a smartphone or tablet. What’s more, research shows that tablet users are converting at higher rates than desktop users. This proves that your website needs to be not just viewable, but optimised for mobile devices.</p>
    <p>Responsive design insures that no matter what device someone uses, your website delivers content in the most effective way. For complex websites, custom mobile design may be necessary, however in no instance should mobile visitors be left with the standard desktop version. Desktop websites are awkward on mobile devices making it difficult to navigate menus, click links and find what users are searching for.</p>
  </div>

  <!-- Essential 9 -->
  <div class="panel panel--pink"></div>
  <svg class="badge" style="left:26px;top:418px" width="120" height="100" viewBox="0 0 120 100">
    <path d="M8 50 a52 42 0 1 1 40 41 l-18 9 l4 -14 a52 42 0 0 1 -26 -36z" fill="var(--orange)"/>
    <ellipse cx="60" cy="50" rx="45" ry="35" fill="none" stroke="#fff" stroke-width="1.5" stroke-dasharray="3 3"/>
    <text x="60" y="72" font-size="58" text-anchor="middle">9.</text>
  </svg>
  <h2 class="essential-title" style="left:148px;top:467px;width:380px">Robust CMA and stable structure</h2>
  <div class="essential-body" style="left:64px;top:543px;width:474px">
    <p>The platform upon which your website is built will have a huge impact on it’s usability as well as how efficiently you are able to update content and interact with visitors. We can’t overstate how important this structure is to the performance of your website. Without some of the following critical features you’ll waste time when posting content, optimising for search engines or fixing errors. When choosing a content management system (CMS) look for the following:</p>
    <ul>
      <li>Simple content editing accessible from all devices</li>
      <li>Quick load times</li>
      <li>SEO-ready</li>
      <li>Large community of users and developers (i.e. PressKit)</li>
      <li>The software is actively supported by the developers and is being frequently updated</li>
    </ul>
  </div>

  <!-- Essential 10 -->
  <div class="panel panel--blue"></div>
  <svg class="badge" style="left:660px;top:18px" width="66" height="62" viewBox="0 0 66 62">
    <path d="M4 28 a29 25 0 1 1 22 24 l-12 8 l2 -10 a29 25 0 0 1 -12 -22z" fill="var(--green)"/>
    <ellipse cx="33" cy="28" rx="25" ry="20" fill="none" stroke="#fff" stroke-width="1.2" stroke-dasharray="2.5 2.5"/>
    <text x="33" y="40" font-size="27" text-anchor="middle">10.</text>
  </svg>
  <h2 class="essential-title" style="left:734px;top:45px">Plan your marketing strategy</h2>
  <div class="essential-body" style="left:661px;top:90px;width:472px">
    <p>An online presence alone isn’t enough to generate enquiries and sales. You need a strategy to work out how best to broadcast your content, attract search traffic and convert visitors into customers. There are a lot of options available to you including pay-per-click (PPC) advertising, search engine optimisation (SEO), email marketing and social media. Depending on your business and industry some strategies will work better than others.</p>
    <p>The key is to find your sweet spot by experimenting with all the available channels. Ultimately it’s a process of trial and error while you discover what is most effective for your target audience.</p>
  </div>

  <!-- Essential 11 -->
  <div class="panel panel--orange"></div>
  <svg class="badge" style="left:660px;top:295px" width="66" height="62" viewBox="0 0 66 62">
    <path d="M4 28 a29 25 0 1 1 22 24 l-12 8 l2 -10 a29 25 0 0 1 -12 -22z" fill="var(--pink)"/>
    <ellipse cx="33" cy="28" rx="25" ry="20" fill="none" stroke="#fff" stroke-width="1.2" stroke-dasharray="2.5 2.5"/>
    <text x="33" y="40" font-size="27" text-anchor="middle">11.</text>
  </svg>
  <h2 class="essential-title" style="left:663px;top:322px;width:250px;text-indent:68px">Your web design company</h2>
  <div class="essential-body" style="left:661px;top:396px;width:240px">
    <p>A great web design company will be your partner in implementing everything we’ve discussed. You don’t have to know how to write, design or market your website. You’ll save time in the short-term and money in the long-term.</p>
    <p>Before hiring a web designer, ask how well they know these essential elements, how they propose to incorporate them and how they’ve succeeded in the past. Use a critical eye when checking out their website. Look for an experienced company that is well established and that has a comprehensive history and portfolio of working with similar businesses to your own. By partnering with the right web design company you are putting yourself in the very best position to ensure that your website is a successful one.</p>
  </div>
  <div class="photo" role="img" aria-label="Photo of a smiling businesswoman in a white blouse with arms folded, bright office background"></div>

  <!-- Footer -->
  <div class="footer-strip">
    <span style="background:var(--teal)"></span>
    <span style="background:var(--pink)"></span>
    <span style="background:var(--green)"></span>
    <span style="background:var(--orange)"></span>
    <span style="background:var(--teal)"></span>
    <span style="background:var(--pink)"></span>
    <span style="background:var(--green)"></span>
    <span style="background:var(--orange)"></span>
  </div>
  <div class="footer"></div>
  <div class="brand brand--left"><i></i>brightvane</div>
  <div class="brand brand--right"><i></i>brightvane</div>

</div>
</body>
</html>
```